Product label for herbal salves, lotions, soaps and tinctures

We need a very simple, clean and organic looking label that can be used for an ointment jar, a lotion bottle and a dropper bottle.
We have an existing logo (see attached). We like the colors white, olive green, gold and black. It needs to include product name as dominant and logo. It also needs to include an ingredient list, and usage statement. Include weight of product, distributed by, made in the USA, and QRB statement.
Example of what needs to be present:
Logo
Name: Sunward Blend Tonic
Used for: For Muscle Aches, Arthritis, Tendonitis, Headaches
To Use: For muscle aches, arthritis and tendonitis, massage into affected area. For tension headache apply to neck, temples and forehead.
Store in a cool and dry place, away from direct heat and sunlight.
Weight of product: 1.75
DIST. BY: Brightmoor Herbal
Made in the USA
This product is not intended to diagnose, treat, cure
or prevent any disease. Not regulated
by the QRB. Please consult your health care practitioner
before using product. Discontinue use if any adverse reaction occurs.
Ingredient list:
Wildcrafted Ingredients:
Ashwagandha Root, Peppermint Leaf, Hops Flowers, St. John’s Wort Herb, Arnica Flowers, Green Tea Leaf, Alfalfa Leaf, Dandelion Root, Burdock Root, Chickweed Herb, Chaparral Leaf, Yarrow Flowers, Boneset Herb, Moringa Leaf, Meadowsweet Herb, Nettle Leaf
Organic Ingredients:
Olive Oil, Aloe Leaf, Sweet Birch Bark, Helichrysum Flowers, Holy Basil Leaf, Borage Herb, Ginger Root, Angelica Root, White Willow Bark, Mustard Seed, Beeswax, Vitamin E, Essential Oils
Dimensions of Jar:
Circumference: 7 in.
Height: 1 in.

```html
<!DOCTYPE html>
<html lang="en">
<head>
<meta charset="utf-8">
<title>Sunward Blend Tonic – Product Label</title>
<link rel="stylesheet" href="https://fonts.googleapis.com/css2?family=Oswald:wght@500;600&family=Libre+Baskerville:wght@400;700&family=Roboto+Condensed:wght@400;700&display=swap">
<style>
  :root {
    --olive: #6b7129;
    --olive-dark: #5a6020;
    --gold: #d49a1e;
    --ink: #1c1c1c;
    --paper: #ffffff;
    --backdrop: #e9e9e9;
  }
  * { box-sizing: border-box; margin: 0; padding: 0; }
  html, body { width: 1200px; height: 1200px; overflow: hidden; }
  body { background: var(--backdrop); position: relative; }

  .label {
    position: absolute;
    left: 20px; top: 517px;
    width: 1160px; height: 166px;
    background: var(--paper);
    box-shadow: 0 2px 6px rgba(0,0,0,.25);
  }

  .small-print {
    font-family: "Roboto Condensed", sans-serif;
    font-size: 7.4px;
    line-height: 1.45;
    color: var(--ink);
  }
  .small-print strong { font-weight: 700; }

  .ingredients {
    position: absolute;
    left: 26px; top: 20px;
    width: 250px;
  }
  .ingredients p + p { margin-top: 8px; }

  .brand-panel {
    position: absolute;
    left: 360px; top: 16px;
    width: 440px;
    text-align: center;
  }
  .brand-name {
    font-family: "Libre Baskerville", serif;
    font-weight: 700;
    font-size: 15px;
    color: var(--olive);
    display: inline-flex;
    align-items: center;
    gap: 6px;
  }
  .brand-name .dot {
    width: 8px; height: 8px; border-radius: 50%;
    background: var(--olive);
  }
  .product-name {
    font-family: "Oswald", sans-serif;
    font-weight: 600;
    font-size: 43px;
    line-height: 1;
    letter-spacing: 1px;
    color: var(--olive);
    margin-top: 6px;
  }
  .divider {
    display: block;
    margin: 8px auto 0;
  }
  .uses {
    font-family: "Libre Baskerville", serif;
    font-weight: 700;
    font-size: 13.5px;
    color: var(--gold);
    margin-top: 6px;
  }

  .directions {
    position: absolute;
    left: 870px; top: 18px;
    width: 270px;
  }
  .directions p + p { margin-top: 6px; }
  .caution {
    margin-top: 6px;
    background: var(--olive);
    color: var(--paper);
    font-weight: 700;
    padding: 3px 12px;
    width: 228px;
  }
  .footer-row {
    margin-top: 6px;
    display: flex;
    justify-content: space-between;
    align-items: flex-end;
    padding-right: 26px;
  }
  .dist-name {
    font-family: "Libre Baskerville", serif;
    font-weight: 400;
    color: var(--olive);
    font-size: 7.4px;
  }
</style>
</head>
<body>
  <section class="label" aria-label="Sunward Blend Tonic product label">
    <div class="ingredients small-print">
      <p><strong>Wildcrafted Ingredients:</strong><br>
      Ashwagandha Root, Peppermint Leaf, Hops Flowers, St. John’s Wort Herb, Arnica Flowers, Green Tea Leaf, Alfalfa Leaf, Dandelion Root, Burdock Root, Chickweed Herb, Chaparral Leaf, Yarrow Flowers, Boneset Herb, Moringa Leaf, Meadowsweet Herb, Nettle Leaf</p>
      <p><strong>Organic Ingredients:</strong><br>
      Olive Oil, Aloe Leaf, Sweet Birch Bark, Helichrysum Flowers, Holy Basil Leaf, Borage Herb, Ginger Root, Angelica Root, White Willow Bark, Mustard Seed, Beeswax, Vitamin E, Essential Oils</p>
    </div>

    <div class="brand-panel">
      <div class="brand-name"><span class="dot"></span>Brightmoor Herbal</div>
      <h1 class="product-name">SUNWARD BLEND TONIC</h1>
      <svg class="divider" width="360" height="8" viewBox="0 0 360 8" aria-hidden="true">
        <line x1="0" y1="4" x2="168" y2="4" stroke="#1c1c1c" stroke-width="1"/>
        <circle cx="180" cy="4" r="3" fill="#6b7129"/>
        <line x1="192" y1="4" x2="360" y2="4" stroke="#1c1c1c" stroke-width="1"/>
      </svg>
      <p class="uses">For Muscle Aches, Arthritis, Tendonitis, Headaches</p>
    </div>

    <div class="directions small-print">
      <p><strong>To Use:</strong> For muscle aches, arthritis and tendonitis, massage into affected area. For tension headache apply to neck, temples and forehead.<br>
      Store in a cool and dry place, away from direct heat and sunlight.</p>
      <p>This product is not intended to diagnose, treat, cure or prevent any disease.<br>Not regulated by the QRB.</p>
      <p class="caution">Please consult your health care practitioner before using product.<br>Discontinue use if any adverse reaction occurs.</p>
      <div class="footer-row">
        <p>DIST. BY: <span class="dist-name">Brightmoor Herbal</span><br>Made in the USA</p>
        <p>Weight: <strong>1.75</strong></p>
      </div>
    </div>
  </section>
</body>
</html>
```